High Quality Flyer Design For Real Estate Website

I require a double sided flyer for the website tallowbrookhomes.net.

The flyer size should be A5.

The flyer must be fresh and up to date and go with the theme of the website.
Updates

Old flyer attachment was missing, but is now attached.

Target Market(s)

Landlords and people looking to buy or sell their house of all age groups

Industry/Entity Type

Real Estate

Font styles to use
Sans Serif

Requirements
Must have
• The main colour of the flyer should be the yellow used on the website.

The logo from the website should also be used (attached)

The text included on the old flyer must be on the new flyer (see attachment)

The flyer should take the reader through a process (see old attached flyer) and make them feel that using the website is very simple.

Nice to have

```html
<!DOCTYPE html>
<html lang="en">
<head>
<meta charset="utf-8">
<title>Tallowbrook Homes – Sell or Rent Flyer</title>
<link rel="stylesheet" href="https://fonts.googleapis.com/css2?family=Russo+One&family=Open+Sans:wght@400;600;700&display=swap">
<style>
  :root {
    --stage: #d9d6d4;
    --paper: #ebebeb;
    --yellow: #fbb816;
    --yellow-light: #ffe200;
    --ink: #1b1b1b;
    --white: #ffffff;
    --photo-dark: #1c231f;
    --photo-glow: #e9e48a;
    --photo-green: #63a21a;
  }
  * { box-sizing: border-box; margin: 0; padding: 0; }
  html, body {
    width: 1200px; height: 960px; overflow: hidden;
    background: var(--stage);
  }
  .flyer {
    position: absolute; left: 100px; top: 120px;
    width: 1000px; height: 720px;
    background: var(--paper);
    overflow: hidden;
    box-shadow: 0 6px 18px rgba(0,0,0,.18);
    font-family: "Open Sans", Arial, sans-serif;
  }
  .flyer-shapes { position: absolute; inset: 0; }
  .brand {
    position: absolute; left: 560px; top: 22px;
    width: 320px; height: 62px;
    background: var(--ink);
    display: flex; flex-direction: column; justify-content: center;
    padding: 0 16px;
  }
  .brand-name {
    display: flex; align-items: center; gap: 10px;
    color: var(--yellow); font-weight: 700; font-size: 22px; line-height: 1;
    white-space: nowrap;
  }
  .brand-mark { width: 14px; height: 14px; background: var(--yellow); flex: none; }
  .brand-tagline {
    color: var(--yellow); font-weight: 700; font-size: 10px; margin-top: 5px; padding-left: 24px;
  }
  .tag-commission {
    position: absolute; left: 580px; top: 112px;
    height: 42px; padding: 0 22px 0 30px;
    background: var(--white); color: var(--ink);
    font-size: 22px; font-weight: 600; line-height: 42px;
    white-space: nowrap;
  }
  .tag-commission::before {
    content: ""; position: absolute; left: 0; top: 0;
    border-top: 21px solid transparent; border-bottom: 21px solid transparent;
    border-left: 16px solid var(--ink);
  }
  .headline-box {
    position: absolute; left: 40px; top: 360px;
    width: 470px; height: 140px;
    background: var(--ink);
    display: flex; align-items: center; padding-left: 36px;
  }
  .headline {
    font-family: "Russo One", Arial, sans-serif;
    color: var(--yellow); font-size: 40px; line-height: 1.15; font-weight: 400;
    white-space: nowrap;
  }
  .subline {
    position: absolute; left: 70px; top: 522px;
    font-family: "Russo One", Arial, sans-serif;
    color: var(--ink); font-size: 34px; line-height: 1.18;
    white-space: nowrap;
  }
  .web-banner {
    position: absolute; left: 0; top: 640px;
    width: 620px; height: 64px;
    display: flex; align-items: center; padding-left: 70px;
    color: var(--ink); font-size: 30px; font-weight: 600;
    white-space: nowrap;
  }
</style>
</head>
<body>
  <main class="flyer">
    <svg class="flyer-shapes" width="1000" height="720" viewBox="0 0 1000 720">
      <defs>
        <linearGradient id="photoTone" x1="0" y1="0" x2="0" y2="1">
          <stop offset="0" stop-color="#1c231f"/>
          <stop offset="0.45" stop-color="#4a4a2e"/>
          <stop offset="0.62" stop-color="#e9e48a"/>
          <stop offset="1" stop-color="#63a21a"/>
        </linearGradient>
      </defs>
      <path class="band-top" d="M380 0 H1000 V170 C860 80 680 60 520 95 C470 60 430 30 380 0 Z" fill="var(--yellow)"/>
      <ellipse cx="560" cy="300" rx="430" ry="248" fill="none" stroke="var(--yellow)" stroke-width="26"/>
      <ellipse cx="560" cy="300" rx="412" ry="234" fill="var(--paper)"/>
      <ellipse cx="560" cy="300" rx="400" ry="225" fill="url(#photoTone)" role="img" aria-label="Photo: two hands passing a small model house over a green field"/>
      <path class="swoosh" d="M260 720 C420 600 700 560 1000 400 V430 C720 590 440 630 300 720 Z" fill="var(--yellow)"/>
      <path class="swoosh-light" d="M640 570 C800 540 920 470 1000 410 V425 C930 490 810 560 640 580 Z" fill="var(--yellow-light)"/>
      <path class="swoosh-small" d="M40 720 C120 640 220 610 300 600 C220 630 150 670 100 720 Z" fill="var(--yellow)"/>
      <path class="banner-bottom" d="M0 640 H640 L600 704 H0 Z" fill="var(--yellow)"/>
    </svg>

    <div class="brand">
      <div class="brand-name"><span class="brand-mark"></span>tallowbrookhomes.net</div>
      <div class="brand-tagline">sell or let with no fees</div>
    </div>

    <div class="tag-commission">Commision Free</div>

    <div class="headline-box">
      <h1 class="headline">SELL OR RENT<br>YOUR PROPERTY</h1>
    </div>

    <p class="subline">&amp; Keep Every Penny<br>Of Your Sale</p>

    <div class="web-banner">www.tallowbrookhomes.net</div>
  </main>
</body>
</html>
```